Gardening and life coaching business card design

I need business cards for a new company in the heart of the Ozarks at the Lake of the Ozarks. Tarsey Brook Unlimited's mission is to teach the world to fish. We provide fresh local fish and produce using permaculture methods. We work with nature and the flow to create more harmony and less impact. We also coach others who are ready to make this transition. We specialize in microgreens and Aquaculture systems. I would like to make Tarsey Brook Unlimited come alive with green vines and purple flowers I wold like Tarsey Brook Unlimited to be in green and the rest of the lettering to be in purple. The feel of the card should be that of the Garden of Eden.

Life Coaching

Tarsey Brook Unlimited
Owner/Operator Delphine Hargrove
Contact Info:
(573) 204-6658
tarseybrookunlimited.com
tarseybrookunlimited is also on FB

```html
<!DOCTYPE html>
<html lang="en">
<head>
<meta charset="utf-8">
<title>Tarsey Brook Unlimited — Business Cards</title>
<link rel="stylesheet" href="https://fonts.googleapis.com/css2?family=Merriweather:wght@400;700&display=swap">
<style>
  :root {
    --backdrop: #4fd6c4;
    --card-white: #f7f7f5;
    --brand-green: #5cbf2a;
    --vine-green: #7cc656;
    --vine-soft: #b9e39a;
    --leaf-deep: #2f7d1f;
    --leaf-light: #a6dc5a;
    --water: #3fb56a;
    --flower-soft: #9a7ad0;
    --ink-purple: #5b2a9c;
    --band-white: rgba(255, 255, 255, 0.93);
  }

  * { box-sizing: border-box; margin: 0; padding: 0; }

  html, body {
    width: 1200px;
    height: 811px;
    overflow: hidden;
  }

  body {
    background: var(--backdrop);
    font-family: "Merriweather", Georgia, serif;
    position: relative;
  }

  .card {
    position: absolute;
    top: 262px;
    width: 500px;
    height: 286px;
    border-radius: 4px;
    box-shadow: 0 10px 24px rgba(0, 60, 50, 0.25);
    overflow: hidden;
  }

  .brand-name {
    font-family: "Merriweather", Georgia, serif;
    font-weight: 400;
    color: var(--brand-green);
    letter-spacing: 0.6px;
    white-space: nowrap;
    line-height: 1;
  }

  /* Ornament zones: vine and flower artwork belongs here */
  .vine-ornament {
    position: absolute;
    border-radius: 14px;
    background: linear-gradient(135deg, var(--vine-soft) 0%, var(--vine-green) 45%, var(--flower-soft) 100%);
    opacity: 0.85;
  }

  /* ---------- front ---------- */
  .card--front { left: 70px; }

  .front-scene {
    position: absolute;
    inset: 0;
    background:
      radial-gradient(ellipse at 70% 30%, var(--leaf-light) 0%, transparent 55%),
      linear-gradient(180deg, var(--leaf-deep) 0%, #4d9f2a 40%, #3c8a2c 55%, var(--water) 75%, #2f9a55 100%);
  }

  .front-banner {
    position: absolute;
    left: 70px;
    top: 113px;
    width: 360px;
    height: 60px;
    background: var(--band-white);
    display: flex;
    align-items: center;
    justify-content: center;
  }

  .front-banner::before,
  .front-banner::after {
    content: "";
    position: absolute;
    left: 12px;
    right: 12px;
    height: 1.5px;
    background: var(--vine-green);
  }
  .front-banner::before { top: 7px; }
  .front-banner::after { bottom: 7px; }

  .front-banner .brand-name { font-size: 22px; }

  .vine-ornament--front-left { left: 40px; top: 84px; width: 58px; height: 40px; }
  .vine-ornament--front-right { left: 400px; top: 162px; width: 58px; height: 40px; }

  /* ---------- back ---------- */
  .card--back {
    left: 630px;
    background: var(--card-white);
  }

  .header-frame {
    position: absolute;
    left: 68px;
    top: 36px;
    width: 364px;
    height: 42px;
    border-top: 1.5px solid var(--vine-green);
    border-bottom: 1.5px solid var(--vine-green);
    display: flex;
    align-items: center;
    justify-content: center;
  }
  .header-frame .brand-name { font-size: 19px; }

  .vine-ornament--back-left { left: 20px; top: 18px; width: 48px; height: 34px; }
  .vine-ornament--back-right { left: 432px; top: 62px; width: 48px; height: 34px; }

  .contact {
    position: absolute;
    left: 44px;
    top: 102px;
    color: var(--ink-purple);
  }

  .contact__name {
    font-size: 22px;
    font-weight: 400;
    line-height: 1.15;
  }

  .contact__role {
    font-size: 12px;
    margin-bottom: 10px;
  }

  .contact__line {
    font-size: 12px;
    line-height: 1.5;
  }
</style>
</head>
<body>

  <section class="card card--front" aria-label="Card front">
    <div class="front-scene" role="img" aria-label="Photograph of a lush green forest reflected in a clear green pool"></div>
    <div class="vine-ornament vine-ornament--front-left" role="img" aria-label="Curling green vine ornament with purple flowers"></div>
    <div class="front-banner">
      <span class="brand-name">Tarsey Brook Unlimited</span>
    </div>
    <div class="vine-ornament vine-ornament--front-right" role="img" aria-label="Curling green vine ornament with purple flowers"></div>
  </section>

  <section class="card card--back" aria-label="Card back">
    <div class="vine-ornament vine-ornament--back-left" role="img" aria-label="Curling green vine ornament with purple flowers"></div>
    <div class="header-frame">
      <span class="brand-name">Tarsey Brook Unlimited</span>
    </div>
    <div class="vine-ornament vine-ornament--back-right" role="img" aria-label="Curling green vine ornament with purple flowers"></div>

    <div class="contact">
      <p class="contact__name">Delphine Hargrove</p>
      <p class="contact__role">Owner/Operator</p>
      <p class="contact__line">T: (573) 204-6658</p>
      <p class="contact__line">W: tarseybrookunlimited.com</p>
      <p class="contact__line">Like us on Kinfolk Social TarseyBrookUnlimited</p>
    </div>
  </section>

</body>
</html>
```